BLRK 2014 Holiday Card

About the Organization: Stone Tales That Shine, LLC helps nature protection and pollution control organizations professionalize and modernize their communications. They assist organizations on fundraising, issue advocacy, or pollution prevention campaigns!

Project Summary: Stone Tales That Shine would like to take stock and thank the amazing group of clients we have worked with and prospects who we are close to closing deals with. BLRK would like to show their appreciation in a holiday card.

Project Timing: BLRK would like to mail the holiday cards by November 14, 2014.

Target Audience: The target audience is the clients that we have worked for this year. They work for environmental organizations. Most are government and non-governmental organizations.
Updates

Please provide inside and outside mock ups. We look forward to reviewing your designs.

Target Market(s)

The target audience is the clients that we have worked for this year. They work for environmental organizations. Most are government and non-governmental organizations.

Industry/Entity Type

Government

Requirements
Must have
• This holiday card must have 4 pages and use the photos as a guide.

Please follow the color and design elements provided in the BLRK_ArtHerdly_StrategyBriefHolidayCard_10102014.pdf.

I also provide the last two holiday cards and some sample image to guide the design.

You have two design choices for our logo. Both are also provided.

```html
<!DOCTYPE html>
<html lang="en">
<head>
<meta charset="utf-8">
<title>Stone Tales That Shine Holiday Card</title>
<link rel="stylesheet" href="https://fonts.googleapis.com/css2?family=Josefin+Sans:wght@300;400&family=Arimo:wght@400;700&display=swap">
<style>
  :root {
    --paper: #ffffff;
    --sea-deep: #0e2f63;
    --sea-mid: #1f5ea8;
    --sea-bright: #3a8fd6;
    --sea-light: #9fd3f2;
    --bubble: rgba(255, 255, 255, 0.22);
    --quote-ink: rgba(255, 255, 255, 0.88);
    --brand-ink: #2a4fa8;
    --contact-ink: #222222;
  }
  * { margin: 0; padding: 0; box-sizing: border-box; }
  html, body {
    width: 1200px;
    height: 900px;
    overflow: hidden;
    background: var(--paper);
  }
  .card-spread {
    position: relative;
    width: 1200px;
    height: 900px;
    display: flex;
  }
  .back-cover {
    position: relative;
    width: 596px;
    height: 900px;
    background: var(--paper);
  }
  .brand {
    position: absolute;
    left: 0;
    width: 596px;
    top: 640px;
    text-align: center;
    font-family: "Arimo", sans-serif;
    font-weight: 700;
    color: var(--brand-ink);
    font-size: 21px;
    line-height: 1.2;
    letter-spacing: 0.5px;
    text-transform: uppercase;
  }
  .brand-mark {
    display: block;
    width: 30px;
    height: 30px;
    margin: 0 auto 14px;
    border-radius: 50%;
    background: var(--brand-ink);
  }
  .contact {
    position: absolute;
    left: 0;
    width: 596px;
    top: 784px;
    text-align: center;
    font-family: "Arimo", sans-serif;
    font-size: 12.5px;
    line-height: 15px;
    color: var(--contact-ink);
    font-style: normal;
  }
  .front-cover {
    position: relative;
    width: 604px;
    height: 900px;
    overflow: hidden;
  }
  .ocean-scene {
    position: absolute;
    inset: 0;
    background:
      radial-gradient(ellipse 420px 340px at 80% 8%, var(--sea-light) 0%, rgba(159, 211, 242, 0) 70%),
      linear-gradient(180deg, var(--sea-bright) 0%, var(--sea-mid) 45%, var(--sea-deep) 100%);
  }
  .quote-bubble {
    position: absolute;
    left: 129px;
    top: 419px;
    width: 396px;
    height: 396px;
    border-radius: 50%;
    background: var(--bubble);
  }
  .quote {
    position: absolute;
    left: 129px;
    top: 484px;
    width: 396px;
    text-align: center;
    font-family: "Josefin Sans", sans-serif;
    font-weight: 300;
    color: var(--quote-ink);
  }
  .quote-line { display: block; }
  .quote-line--soft {
    font-size: 31px;
    line-height: 57px;
    letter-spacing: 1px;
  }
  .quote-line--strong {
    font-size: 52px;
    line-height: 64px;
    margin-top: 6px;
    letter-spacing: 1px;
  }
  .quote-line--caps {
    font-size: 31px;
    line-height: 46px;
    letter-spacing: 2px;
  }
  .quote-author {
    display: block;
    margin-top: 18px;
    font-size: 20px;
    letter-spacing: 1px;
    font-style: normal;
  }
</style>
</head>
<body>
  <main class="card-spread">
    <section class="back-cover">
      <div class="brand">
        <span class="brand-mark" aria-hidden="true"></span>
        Stone Tales<br>That Shine
      </div>
      <address class="contact">
        Stone Tales That Shine, LLC<br>
        412 Larkspur Lane, Suite 108<br>
        Harlow Bay, OR 97455<br>
        800-555-0147<br>
        stonetalesthatshine.com
      </address>
    </section>
    <section class="front-cover">
      <div class="ocean-scene" role="img" aria-label="Underwater illustration of a school of dark fish swimming through blue water with light from the surface and rising bubbles"></div>
      <div class="quote-bubble" aria-hidden="true"></div>
      <blockquote class="quote">
        <span class="quote-line quote-line--soft">Individually,</span>
        <span class="quote-line quote-line--soft">we are one drop.</span>
        <span class="quote-line quote-line--strong">TOGETHER,</span>
        <span class="quote-line quote-line--caps">WE ARE AN OCEAN.</span>
        <cite class="quote-author">Haruki Tenmaro</cite>
      </blockquote>
    </section>
  </main>
</body>
</html>
```